Manuka honey jar label for new Manuka brand

We are planning to start a Manuka honey brand and we need to design the label for the honey jar. Manuka honey is an up and coming product and the market is still young in our country.
Our market is dominated by 1 brand: Korivo Vital (photo attached). To the people who know what Manuka honey is, they associate it with Korivo Vital in the same way people associate Cola with Zibo Zesta or printer copies with Pluvex.
The good news is that a lot of people do not know yet what Manuka honey is and we still have the opportunity of being the first brand they get to know. At the same time, we still need to be able to take at least a bite out of the Korivo Vital market share.
The Korivo Vital label for their jar I think is not just absolutely gorgeous but it also does its job extremely well. It only features 3 informations:
- name of brand/logo (Korivo Vital)
- name of product (Manuka Honey)
- and mgo rating which is like a rating of how strong the honey is
By having just this information on a relatively small label, their label SCREAMS Manuka by having the Manuka words twice (the brand and the product name) and people develop this association between Korivo Vital and Manuka products in general.
Our product will also be in a similar square plastic jar. It will also be dark tinted, that´s important to note. We can also go for a blue cap but in order to differentiate ourselves from Korivo Vital we thought of maybe choosing a black lid instead. I uploaded 2 jars, 1 with black lid and 1 with gold (although it looks more like mustard) that you can use for simulations. They are pretty accurate of the type of jars and lids that we can have.
The label has total length of about 20cm. One side of the jar has 5,5 cm of the label and the height of the label is 4,5 cm. We can also use selective gold laminating on the label but we cannot have custom shape label at this point as Korivo Vital does with its tree logo that sticks outside the label.
I need the design for the entire label but the focus should be on the front part, that is the part that sells and catches your eye. Like Korivo Vital, the front part I want to have 3 vital informations:
- name of brand/logo (in our case Halvern Terra) - we do not have a pre-existing logo, this needs to be created alongside the label
- and mgo rating
As "other" information we also need the net weight "250 g" alongside with the typical "e" to appear on the front. That is a legal requirement.
Optionally, you can add a small phrase somewhere like "Harvested in New Zealand" or "Made in New Zealand" since this is a product that is only made there and in some areas of Australia.
This is pretty much all the info. As a final note, there are a ton of beautiful premium Manuka honey jar labels. But they are too fancy and when you look at them you don´t instantly recognize that it is Manuka Honey.
This instant recognition is vital! With this small jar there is the danger for customers to think that maybe it´s medicine, maybe it´s sports supplements etc. This is a relatively small product and imagine you just glance on it on the retail shelf. Instantly you must think it is Manuka Honey and that it is beautiful. And if you see it on the shelf next to Korivo Vital, it would be best to also think that you would rather buy this (it gives you more trust) than the Korivo Vital.
One final note: I do not want the bee as an insect on the label. I think some people are turned off when they see an insect with its small legs and make a bad association that there are insects inside. I do not mind symbolism or somehow super stylized bee in a modern way, but I do not want a plain insect on the label.
For any other questions, I am at your disposal. Thank you very much for taking the time to send us a proposal!

```html
<!DOCTYPE html>
<html lang="en">
<head>
<meta charset="utf-8">
<title>Halvern Terra – Manuka Honey Label</title>
<link rel="stylesheet" href="https://fonts.googleapis.com/css2?family=Quicksand:wght@500;600&family=Poppins:wght@800&display=swap">
<style>
  :root {
    --backdrop: #e6cfad;
    --honey-light: #eba21a;
    --honey: #e2900c;
    --honey-deep: #c9740a;
    --comb: #c4761c;
    --brown: #a25a1c;
    --white: #ffffff;
  }
  * { margin: 0; padding: 0; box-sizing: border-box; }
  html, body {
    width: 1200px;
    height: 800px;
    overflow: hidden;
    background: var(--backdrop);
  }
  .canvas {
    position: relative;
    width: 1200px;
    height: 800px;
  }
  .label-front {
    position: absolute;
    left: 300px;
    top: 130px;
    width: 600px;
    height: 540px;
    border-radius: 6px;
    background: linear-gradient(180deg, var(--honey-light) 0%, var(--honey) 55%, var(--honey-deep) 100%);
    overflow: hidden;
    color: var(--white);
  }
  .comb-area {
    position: absolute;
    left: 300px;
    top: 50px;
    width: 255px;
    height: 440px;
    background: radial-gradient(ellipse at 75% 40%, rgba(196,118,28,0.55) 0%, rgba(196,118,28,0.25) 45%, rgba(196,118,28,0) 75%);
  }
  .label-edge {
    position: absolute;
    right: 0;
    top: 30px;
    width: 40px;
    height: 450px;
    background: #ececec;
    border-radius: 14px 0 0 14px;
  }
  .brand {
    position: absolute;
    left: 52px;
    top: 70px;
  }
  .brand-mark {
    width: 96px;
    height: 96px;
    border-radius: 50%;
    background: var(--white);
    margin-bottom: 22px;
  }
  .brand-name {
    font-family: "Quicksand", sans-serif;
    font-weight: 500;
    font-size: 46px;
    line-height: 1.05;
    letter-spacing: 0.5px;
  }
  .mgo-badge {
    position: absolute;
    left: 56px;
    top: 345px;
    width: 64px;
    height: 74px;
  }
  .mgo-badge text {
    font-family: "Quicksand", sans-serif;
    font-weight: 600;
    text-anchor: middle;
  }
  .product-name {
    position: absolute;
    right: 58px;
    top: 355px;
    font-family: "Poppins", sans-serif;
    font-weight: 800;
    font-size: 56px;
    line-height: 1.05;
    text-align: right;
  }
  .footer {
    position: absolute;
    left: 52px;
    bottom: 36px;
    display: flex;
    align-items: center;
    gap: 12px;
    font-family: "Quicksand", sans-serif;
  }
  .net-weight {
    font-size: 26px;
    font-weight: 600;
  }
  .divider {
    width: 2px;
    height: 30px;
    background: var(--white);
  }
  .origin {
    font-size: 13px;
    font-weight: 600;
    line-height: 1.2;
  }
</style>
</head>
<body>
  <main class="canvas">
    <section class="label-front">
      <div class="comb-area" role="img" aria-label="Scattered honeycomb hexagon pattern in deep amber tones"></div>
      <div class="label-edge"></div>

      <div class="brand">
        <div class="brand-mark"></div>
        <p class="brand-name">Halvern<br>Terra</p>
      </div>

      <svg class="mgo-badge" viewBox="0 0 64 74" aria-label="MGO 250 rating">
        <polygon points="32,2 62,19 62,55 32,72 2,55 2,19" fill="var(--white)"/>
        <polygon points="2,38 62,30 62,55 32,72 2,55" fill="var(--brown)"/>
        <text x="32" y="28" font-size="15" fill="var(--brown)">250</text>
        <text x="32" y="57" font-size="13" fill="var(--white)">MGO</text>
      </svg>

      <h1 class="product-name">Manuka<br>Honey</h1>

      <div class="footer">
        <span class="net-weight">250g</span>
        <span class="divider"></span>
        <span class="origin">Harvested in<br>New Zealand</span>
      </div>
    </section>
  </main>
</body>
</html>
```